Brochure for medical doctor

I need a brochure for a medical doctor to promote his practice. The brochure should contain his picture, business information (use letterhead from attachment), and the following text:

- Now accepting PI cases on lien!
- Same and next business day appointments available for initial visits, pre-operative clearances, and all other medical needs

- Expedited medical reports sent quickly to your office

Medical

```html
<!DOCTYPE html>
<html lang="en">
<head>
<meta charset="utf-8">
<title>Meadowbrook Medical Center Flyer</title>
<link rel="stylesheet" href="https://fonts.googleapis.com/css2?family=Oswald:wght@300;400;500;600&family=Open+Sans:wght@400;600;700&display=swap">
<style>
  :root {
    --red: #d71f26;
    --dark: #2b2b2d;
    --band: #3b3b3d;
    --grey-text: #666;
    --page-bg: #e9e9e9;
    --paper: #ffffff;
  }
  html, body {
    margin: 0; padding: 0;
    width: 1200px; height: 772px;
    overflow: hidden;
    background: var(--page-bg);
    font-family: "Open Sans", sans-serif;
  }
  .flyer {
    position: absolute;
    left: 308px; top: 6px;
    width: 612px; height: 792px;
    transform: scale(0.955);
    transform-origin: top left;
    background: var(--paper);
    overflow: hidden;
    box-shadow: 0 2px 10px rgba(0,0,0,.18);
  }
  .flyer-art { position: absolute; inset: 0; }
  .brand {
    position: absolute; left: 28px; top: 36px;
    display: flex; align-items: center; gap: 8px;
  }
  .brand-mark { width: 32px; height: 32px; background: var(--red); }
  .brand-name {
    font-family: "Oswald", sans-serif; font-weight: 500;
    color: var(--dark); font-size: 18px; line-height: 1.1;
    letter-spacing: .2px; text-transform: uppercase;
  }
  .headline {
    position: absolute; left: 24px; top: 176px; margin: 0;
    font-family: "Oswald", sans-serif; font-weight: 600;
    font-size: 36px; line-height: 50px; text-transform: uppercase;
    letter-spacing: -.6px;
    transform: scaleX(0.89); transform-origin: left top;
    white-space: nowrap;
  }
  .headline .accent { color: var(--red); display: block; }
  .headline .main { color: var(--dark); display: block; font-weight: 500; }
  .intro {
    position: absolute; left: 0; top: 522px; width: 612px; margin: 0;
    text-align: center; font-size: 17.5px; line-height: 23px; color: #222;
  }
  .cta-pill {
    position: absolute; left: 44px; top: 587px;
    width: 517px; height: 36px; border-radius: 18px;
    background: var(--red); color: #fff;
    font-weight: 700; font-size: 14.5px; letter-spacing: .2px;
    display: flex; align-items: center; justify-content: center;
    box-shadow: 0 2px 5px rgba(0,0,0,.2);
  }
  .address {
    position: absolute; left: 0; top: 630px; width: 612px;
    text-align: center; font-size: 14px; color: #222;
  }
  .hours {
    position: absolute; left: 0; top: 657px; width: 612px;
    text-align: center; font-size: 11px; color: var(--grey-text);
  }
  .doctor-band {
    position: absolute; left: 0; top: 695px; width: 612px; height: 63px;
    background: var(--band);
  }
  .doctor-photo {
    position: absolute; left: 18px; top: 654px;
    width: 126px; height: 126px; border-radius: 50%;
    border: 4px solid #fff; box-sizing: border-box;
    background: radial-gradient(circle at 50% 40%, #c9a88a 0%, #7c6a5c 55%, #4b4542 100%);
    box-shadow: 0 0 0 1px #ccc;
  }
  .doctor-name {
    position: absolute; left: 166px; top: 702px;
    font-family: "Oswald", sans-serif; font-weight: 300;
    font-size: 20px; color: #fff;
  }
  .doctor-title {
    position: absolute; left: 166px; top: 731px;
    font-size: 12px; color: #fff;
  }
  .appt-label {
    position: absolute; right: 12px; top: 708px;
    font-size: 12px; color: #fff;
  }
  .call-tab {
    position: absolute; right: 0; top: 727px; width: 236px; height: 31px;
    background: var(--red);
    clip-path: polygon(22px 0, 100% 0, 100% 100%, 0 100%);
    color: #fff; font-weight: 700; font-size: 15px;
    display: flex; align-items: center; justify-content: flex-end;
    padding-right: 12px; box-sizing: border-box;
  }
  .website {
    position: absolute; left: 0; top: 766px; width: 612px;
    text-align: center; font-size: 13px; letter-spacing: .6px; color: #222;
  }
  .website .domain { color: var(--red); font-weight: 600; }
</style>
</head>
<body>
  <main class="flyer">
    <svg class="flyer-art" width="612" height="792" viewBox="0 0 612 792">
      <defs>
        <radialGradient id="bubble" cx="45%" cy="40%" r="60%">
          <stop offset="0" stop-color="#ffffff"/>
          <stop offset="0.75" stop-color="#f1f1f1"/>
          <stop offset="1" stop-color="#dedede"/>
        </radialGradient>
        <linearGradient id="family" x1="0" y1="0" x2="1" y2="1">
          <stop offset="0" stop-color="#c99a80"/>
          <stop offset="0.45" stop-color="#e3c2ad"/>
          <stop offset="0.8" stop-color="#7fb6cf"/>
          <stop offset="1" stop-color="#5e8fb0"/>
        </linearGradient>
      </defs>
      <rect x="0" y="0" width="612" height="792" fill="#fff"/>
      <path d="M345,0 L612,0 L612,470 C520,490 400,478 330,420 C262,362 232,200 345,0 Z"
            fill="url(#family)" role="img" aria-label="Photo of a smiling multi-generation family"/>
      <path class="swoosh" d="M335,0 C222,190 248,370 318,430 C392,494 525,508 612,496 L612,470 C520,490 400,478 330,420 C262,362 232,200 345,0 Z"
            fill="var(--red)"/>
      <circle cx="121" cy="241" r="126" fill="url(#bubble)"/>
      <circle cx="212" cy="388" r="88" fill="#eef0ee" stroke="#cfcfcf" stroke-width="1.5"
              role="img" aria-label="Street map showing the clinic location"/>
      <path d="M205,378 a7,7 0 1 1 14,0 c0,6 -7,12 -7,12 s-7,-6 -7,-12 Z" fill="var(--red)"/>
      <circle cx="212" cy="378" r="2.5" fill="#fff"/>
    </svg>

    <div class="brand">
      <span class="brand-mark"></span>
      <span class="brand-name">Meadowbrook Medical<br>Center</span>
    </div>

    <h1 class="headline">
      <span class="accent">Now Accepting</span>
      <span class="main">PI Cases on Lien!</span>
    </h1>

    <p class="intro">Same and next business day appointments available for initial visits,<br>pre-operative clearances, and all other medical needs</p>

    <div class="cta-pill">EXPEDITED MEDICAL REPORTS SENT QUICKLY TO YOUR OFFICE</div>

    <div class="address">4150 Linden Ave. Oak Valley, CA 90000</div>
    <div class="hours">Mon-Fri : 9:00 am - 5:00 pm Saturday &amp; Sunday Closed</div>

    <div class="doctor-band"></div>
    <div class="doctor-photo" role="img" aria-label="Portrait of the physician in a white coat"></div>
    <div class="doctor-name">Daniel Reyes, M.D.</div>
    <div class="doctor-title">Family Practice Physician</div>
    <div class="appt-label">APPOINTMENT</div>
    <div class="call-tab">CALL US : (555) 014-2288</div>

    <div class="website">www.<span class="domain">MeadowbrookMedical</span>.com</div>
  </main>
</body>
</html>
```